Book Cover design

The book title is Rain falls slowly on quiet gardens

I need a book cover design for a book about the unexpected loss of child. The book is a journal of my first 12 months after the loss of my son. An expression of how the grief never ends you just learn to cope. The journey to healing and hope.
Updates

Change in book title

Target Market(s)

Anyone that has experienced loss of love, career, physical loss, PTSD or experienced losing someone in an untimely manner

Font styles to use
Serif

Colors
0456a4
0792cd
33b8a4
acd136
ffffff
cee9f5
cfdeed

Requirements
Must have
• Beauty Depth

```html
<!DOCTYPE html>
<html lang="en">
<head>
<meta charset="utf-8">
<title>Rain falls slowly on quiet gardens – Book Cover</title>
<link rel="stylesheet" href="https://fonts.googleapis.com/css2?family=Cormorant+Garamond:wght@500;600&display=swap">
<style>
  :root {
    --backdrop: #3a9fd0;
    --cover-dark: #2f2f2f;
    --cover-mid: #3d3d3d;
    --cover-light: #8a8a8a;
    --title-white: #ffffff;
    --title-shadow: rgba(0, 0, 0, 0.55);
    --subtitle: #cee9f5;
    --band-light: #cfdeed;
    --band-shade: #a9b8c7;
    --author-ink: #0456a4;
    --orb-core: #f3c8a4;
    --orb-pink: #c990a8;
    --orb-mid: #5a3f86;
    --orb-deep: #22204f;
    --orb-rim: #0792cd;
    --orb-line: #1a1a1a;
  }

  html, body {
    margin: 0;
    padding: 0;
    width: 1200px;
    height: 800px;
    overflow: hidden;
    background: var(--backdrop);
  }

  .canvas {
    position: relative;
    width: 1200px;
    height: 800px;
    background: var(--backdrop);
  }

  .cover {
    position: absolute;
    left: 400px;
    top: 40px;
    width: 400px;
    height: 720px;
    background: linear-gradient(225deg, var(--cover-light) 0%, var(--cover-mid) 45%, var(--cover-dark) 100%);
    overflow: hidden;
  }

  .cover__title {
    position: absolute;
    left: 0;
    right: 0;
    top: 26px;
    margin: 0;
    text-align: center;
    font-family: "Cormorant Garamond", serif;
    font-weight: 600;
    color: var(--title-white);
    text-shadow: 3px 4px 4px var(--title-shadow);
    line-height: 1;
  }

  .cover__title-line {
    display: block;
    font-size: 32px;
    letter-spacing: 0.2em;
    padding-left: 0.2em;
    margin-bottom: 10px;
  }

  .cover__artwork {
    position: absolute;
    left: 68px;
    top: 170px;
    width: 250px;
    height: 280px;
  }

  .cover__tagline {
    position: absolute;
    left: 0;
    right: 0;
    top: 460px;
    margin: 0;
    text-align: center;
    font-family: "Cormorant Garamond", serif;
    font-weight: 500;
    font-size: 22px;
    color: var(--subtitle);
  }

  .cover__author-band {
    position: absolute;
    left: 6px;
    right: 6px;
    top: 500px;
    bottom: 0;
    background: linear-gradient(90deg, var(--band-shade) 0%, var(--band-light) 18%, var(--band-light) 100%);
  }

  .cover__author {
    position: absolute;
    left: 0;
    right: 0;
    bottom: 40px;
    margin: 0;
    text-align: center;
    font-family: "Cormorant Garamond", serif;
    font-weight: 600;
    font-size: 42px;
    color: var(--author-ink);
  }
</style>
</head>
<body>
<main class="canvas">
  <article class="cover">
    <h1 class="cover__title">
      <span class="cover__title-line">RAIN FALLS</span>
      <span class="cover__title-line">SLOWLY ON</span>
      <span class="cover__title-line">QUIET GARDENS</span>
    </h1>

    <svg class="cover__artwork" viewBox="0 0 250 280" role="img" aria-label="Glowing illustration of an unborn baby curled inside a round womb">
      <defs>
        <radialGradient id="orb-glow" cx="0.5" cy="0.42" r="0.6">
          <stop offset="0" stop-color="var(--orb-core)"/>
          <stop offset="0.35" stop-color="var(--orb-pink)"/>
          <stop offset="0.65" stop-color="var(--orb-mid)"/>
          <stop offset="0.9" stop-color="var(--orb-deep)"/>
          <stop offset="1" stop-color="var(--orb-rim)"/>
        </radialGradient>
      </defs>
      <ellipse cx="125" cy="140" rx="121" ry="136" fill="url(#orb-glow)" stroke="var(--orb-line)" stroke-width="4"/>
    </svg>

    <p class="cover__tagline">...the journey to healing and hope</p>

    <div class="cover__author-band">
      <p class="cover__author">Author Name</p>
    </div>
  </article>
</main>
</body>
</html>
```